依頼概要
本サービスの集客用FAXDMのデザインをお願い致します。

■コンセプト
「冷凍食品専門の物流倉庫!機能充実した最新設備が特長です」
※参考、物流倉庫サービスとは:https://www.kawanami-corp.jp/hokanbox/post-218

■ターゲット像:
★「冷凍食品・冷蔵食材」を扱う企業
・倉庫の確保がしたい物流会社も許容
→メーカー、卸売業者、EC業者などの区分は問わない。
→「飲食店」「食品メーカー」「農業」「卸会社」「物流会社」のリストに配布予定。

■ターゲットが保有するニーズ、あるいは課題
・品質管理のために高い冷凍機能が無いといけない。
・作業品質が悪く、納期遅延や破損・汚損が発生する。
・作業に忙殺されてしまっている。
・業績拡大に合わせて倉庫を拡張したい

■訴求するベネフィット:
①最新設備があって冷凍機能〇、その他の機能も〇。
②素晴らしい設備があるので、作業品質は万全。リソースも十分。
③埼玉県の好立地に広大な倉庫があります。首都圏にもスムーズに配送
④1個、1パレット、1日の小規模案件も喜んでご対応
⑤特定の期間のみ発送を強化してほしいなど柔軟に対応します。
→「衝撃のプライス!」のように価格を強く訴求することも可
→入庫料は無料

■その他、参考表現:
・埼玉県加須市に冷凍倉庫が出来ました
・保管商品を大募集しています
・1日からでも使えます
・費用は格安、保管費用は1パレット1日40円~(税込44円)から
(※パレットとは縦110cm×横110cmの保管単位です)
・ピッキングや発送業務も承ります

■必須の項目:
・相手の社名、担当者名、電話番号、メールアドレスを書く欄
・問い合わせ先として「受付センターの電話番号とFAX番号」を記載
TEL:0120-731-904/FAX:0280-47-9163
グリーンウェーブ受付センター 埼玉県加須市松葉912
受付時間9:00~18:00(日・3が日除く)

幅広く複数案の採用を考えています。
参考資料として、これまでのFAXDMデザインをお送り致します。

以上です。
■ 選んだ理由

弊社の雰囲気に合ったデザインを選ばせていただきました。FAXDM用ですので小さい字ではなく大きな字でわかりやすいデザインが良かったです。

■ 提案者全員のお礼・コメント

ありがとうございました。次回の制作予定ががありましたら積極的に本サイトを利用させていただきます。

```html
<!DOCTYPE html>
<html lang="ja">
<head>
<meta charset="utf-8">
<title>物流倉庫誕生 FAXDM</title>
<link rel="stylesheet" href="https://fonts.googleapis.com/css2?family=Noto+Sans+JP:wght@400;500;700;900&display=swap">
<style>
:root{
  --ink:#111;
  --paper:#fff;
  --mid:#8a8a8a;
  --light:#d9d9d9;
}
*{box-sizing:border-box;margin:0;padding:0}
html,body{width:850px;height:1200px;overflow:hidden;background:var(--paper)}
body{font-family:"Noto Sans JP",sans-serif;color:var(--ink)}
.sheet{width:850px;height:1200px;padding:22px 30px;display:flex;flex-direction:column;gap:10px}

.targets{display:flex;gap:8px;height:40px}
.targets li{list-style:none;border:2px solid var(--ink);font-weight:900;font-size:21px;display:flex;align-items:center;justify-content:center;padding:0 10px}
.targets li:first-child{flex:1.7}
.targets li{flex:1}

.hero{height:200px;display:flex;gap:18px;align-items:center;position:relative}
.warehouse{width:230px;height:180px;position:relative}
.warehouse-art{position:absolute;inset:0;background:linear-gradient(#9a9a9a,#6f6f6f);clip-path:polygon(0 30%,50% 0,100% 30%,100% 100%,0 100%)}
.warehouse-place{position:absolute;left:0;right:0;top:70px;text-align:center;color:var(--paper);font-weight:900;font-size:26px;line-height:1.2}
.headline{font-weight:900;font-size:92px;line-height:1.02;letter-spacing:2px}
.badge-frozen{position:absolute;right:0;top:92px;width:120px;height:100px;border:3px solid var(--ink);border-radius:50%;display:flex;align-items:center;justify-content:center;text-align:center;font-weight:900;font-size:22px;line-height:1.2;background:var(--paper)}

.band{background:var(--ink);color:var(--paper);font-weight:900;display:flex;align-items:center;position:relative}
.band-recruit{height:70px;font-size:48px;padding-left:18px;letter-spacing:3px}
.badge-free{position:absolute;right:10px;top:-14px;width:120px;height:98px;border-radius:50%;background:var(--paper);color:var(--ink);border:3px solid var(--ink);display:flex;align-items:center;justify-content:center;text-align:center;font-size:22px;line-height:1.25}

.offers{height:150px;display:flex;gap:10px}
.offer-price{width:260px;font-weight:700}
.offer-price .label{font-size:20px;font-weight:900;display:flex;align-items:center;gap:8px}
.offer-price .cheap{background:var(--ink);color:var(--paper);font-size:16px;padding:2px 6px}
.offer-price .amount{font-size:28px;font-weight:900;line-height:1.3}
.offer-price .amount small{font-size:15px}
.offer-price .note{font-size:12px;font-weight:500;line-height:1.4}
.offer-box{border:2px solid var(--ink);font-weight:900;display:flex;align-items:center;justify-content:center;text-align:center;line-height:1.3}
.offer-day{width:120px;font-size:23px}
.offer-pick{width:150px;font-size:19px}
.worker{flex:1;position:relative}
.worker-art{position:absolute;left:60px;right:0;top:10px;bottom:0;background:linear-gradient(#bdbdbd,#8a8a8a)}
.worker-bubble{position:absolute;left:0;top:0;width:92px;height:92px;border-radius:50%;border:2px solid var(--ink);background:var(--paper);display:flex;align-items:center;justify-content:center;text-align:center;font-size:13px;font-weight:900;line-height:1.3}

.band-trouble{height:50px;font-size:30px;padding-left:18px}
.troubles{height:100px;display:flex;gap:10px}
.troubles li{list-style:none;flex:1;border:2px solid var(--ink);display:flex;align-items:center;justify-content:center;text-align:center;font-weight:700;font-size:17px;line-height:1.35;padding:6px}

.benefits{height:130px;display:flex;flex-direction:column;justify-content:space-between}
.benefits li{list-style:none;font-size:20px;font-weight:700;display:flex;align-items:center;gap:8px}
.benefits li::before{content:"";width:14px;height:14px;border-radius:50%;background:var(--ink);flex:none}

.order{border:2px solid var(--ink);display:flex;flex-direction:column}
.order-head{height:60px;display:flex;align-items:center;gap:18px;padding:0 14px;border-bottom:2px solid var(--ink)}
.order-lead{font-size:16px;font-weight:700;line-height:1.2;border:2px solid var(--ink);padding:4px 8px}
.order-fax{font-size:44px;font-weight:900;letter-spacing:1px}
.order-hint{font-size:12px;font-weight:500;line-height:1.3;margin-left:auto}
.order-form{display:grid;grid-template-columns:100px 1fr 100px 1fr;grid-auto-rows:40px}
.order-form div{border-right:1px solid var(--ink);border-bottom:1px solid var(--ink);font-size:15px;font-weight:700;display:flex;align-items:center;padding:0 10px}
.order-form .key{background:var(--light)}
.order-form .wide{grid-column:span 3}
.order-form div:nth-last-child(-n+4){border-bottom:none}

.contact{height:104px;border-top:3px solid var(--ink);display:flex;align-items:center;gap:16px;padding-top:8px}
.contact-tag{background:var(--ink);color:var(--paper);font-weight:900;font-size:17px;line-height:1.25;padding:10px 8px;text-align:center}
.contact-center{font-weight:900;font-size:22px;line-height:1.4}
.contact-center small{display:block;font-size:15px;font-weight:500}
.contact-tel{display:flex;flex-direction:column;font-weight:900}
.contact-tel .free{font-size:34px;display:flex;align-items:center;gap:6px}
.contact-tel .fax{font-size:18px;font-weight:700}
.contact-hours{font-size:13px;font-weight:500;line-height:1.4;margin-left:auto}
</style>
</head>
<body>
<main class="sheet">
  <ul class="targets">
    <li>食品・食材を扱う企業様</li>
    <li>メーカー様</li>
    <li>卸売業者様</li>
    <li>EC業者様</li>
  </ul>

  <section class="hero">
    <div class="warehouse">
      <div class="warehouse-art" role="img" aria-label="倉庫の建物のイラスト"></div>
      <p class="warehouse-place">埼玉県<br>加須市に</p>
    </div>
    <h1 class="headline">物流倉庫<br>誕生!!</h1>
    <p class="badge-frozen">冷凍食品<br>OK!</p>
  </section>

  <h2 class="band band-recruit">保管商品を大募集<span class="badge-free">入庫料<br>無料!</span></h2>

  <section class="offers">
    <div class="offer-price">
      <p class="label">保管費用は<span class="cheap">格安</span></p>
      <p class="amount">1パレット1日40円~<br><small>(税込44円)</small></p>
      <p class="note">※パレットとは<br>縦110cm×横110cmの保管単位です</p>
    </div>
    <p class="offer-box offer-day">1日・1個<br>からでも<br>OK!</p>
    <p class="offer-box offer-pick">ピッキング作業や<br>発送業務も<br>承ります!</p>
    <div class="worker">
      <div class="worker-art" role="img" aria-label="台車を押して荷物を運ぶ作業員のイラスト"></div>
      <p class="worker-bubble">レンタル<br>倉庫とは<br>ここが違う!</p>
    </div>
  </section>

  <h2 class="band band-trouble">こんな事でお困りではありませんか?</h2>

  <ul class="troubles">
    <li>品質管理に<br>高い冷凍機能<br>が必要。</li>
    <li>作業現場が悪く、<br>納期の遅延や破損<br>汚損が発生する。</li>
    <li>日々作業に<br>忙殺されて<br>いる。</li>
    <li>業績拡大に<br>合わせ倉庫を<br>拡張したい。</li>
  </ul>

  <ul class="benefits">
    <li>冷凍の他、最新設備で作業品質は万全。リソースも十分。</li>
    <li>埼玉県の好立地に立つ広大な倉庫は首都圏にもスムーズに配送可能。</li>
    <li>1個、1パレット、1日の小規模案件も喜んでご対応。</li>
    <li>特定の期間のみ発送を強化してほしいなど柔軟に対応。</li>
  </ul>

  <section class="order">
    <div class="order-head">
      <p class="order-lead">お申し込みは<br>こちらまで</p>
      <p class="order-fax">FAX.0280-47-9163</p>
      <p class="order-hint">下記必要事項を<br>ご記入の上FAXください</p>
    </div>
    <div class="order-form">
      <div class="key">御社名</div><div></div>
      <div class="key">ご担当者名</div><div></div>
      <div class="key">ご住所</div><div class="wide">〒</div>
      <div class="key">TEL</div><div></div>
      <div class="key">メール<br>アドレス</div><div></div>
    </div>
  </section>

  <footer class="contact">
    <p class="contact-tag">お問い<br>合わせ</p>
    <p class="contact-center">グリーンウェーブ受付センター<small>埼玉県加須市松葉912</small></p>
    <div class="contact-tel">
      <p class="free">
        <svg width="30" height="30" viewBox="0 0 24 24" aria-hidden="true"><path fill="#111" d="M6.6 10.8a15.1 15.1 0 0 0 6.6 6.6l2.2-2.2c.3-.3.7-.4 1-.2 1.1.4 2.3.6 3.6.6.6 0 1 .4 1 1V20c0 .6-.4 1-1 1A17 17 0 0 1 3 4c0-.6.4-1 1-1h3.5c.6 0 1 .4 1 1 0 1.3.2 2.5.6 3.6.1.3 0 .7-.2 1z"/></svg>
        0120-731-904
      </p>
      <p class="fax">FAX 0280-47-9163</p>
    </div>
    <p class="contact-hours">受付時間<br>9:00~18:00<br>(日・3が日除く)</p>
  </footer>
</main>
</body>
</html>
```